Brochure Willowmere Care Partners

Brochure 12 x 9 tri fold with insert/ Rack card 9x4. Willowmere Care Partners 318 Fernbrook Lane Easton, MD 21629410-822-2207AgingAtHomeSolution.com Tag: Devoted to Steadfast Household Support.
What we do: Home care agency that services higher end Clients Artsy area on the water. Taking care of seniors in their home.

Our story: Opening Willowmere Care Partners, Inc. is my way of making a difference in an industry that is dominated by franchises that often have their policies dictated by corporate policy-makers who are unfamiliar with local customs. My goal is to raise the level of non-medical home health care in our area by providing additional, customized training, higher wages for our care-partners and an inclusive workforce in the decision-making process when developing customized care planning for our clients. Through collaboration with the client, their family and care-partners I have learned what issues, concerns and disappointments may arise which enables me to provide a more defined solution for those in need.My goal of providing superior training required locating a nationally recognized curriculum that would serve our clients’ needs. I found the perfect fit with Ranella Vosk’s, Bright Path in Caregiving™ and her Shining Stones Method™. These programs provide our care-partners with the tools needed to handle the challenges of natural aging and living with Dementia. I was so impressed with these programs, I became a Certified Independent Trainer; one of five in the State of Maryland. There is a bonus for our care-partners who are required to maintain Continuing Education Units - these programs qualify for credit! Improving our industry by providing exemplary care-partners is my goal!I look forward to assisting you with your needs! Dora Pruitt Owner

Services: Companion Care Service - Conversation and Companionship , Meal Preparation, Light House Keeping, Errand Service ,Grocery Shopping ,Incidental Transportation, Laundry & Linen Washing, Medication Reminders, Recreational Activities ,
Personal Care Services: Bathing ,Mobility ,Transferring & Positioning ,Incontinence Care ,Oral Hygiene ,Feeding, Toileting ,Grooming & Dressing, Special Diet Preparation.

Our Commitment to You: Extensive Care-Partner Education - We provide, in addition to state mandated training, eight additional hours of hands-on Dementia training from a Certified, Independent Instructor on the “Bright Path in Caregiving” by Ranella Vosk, a nationally recognized instructor on aging.

Nutrition/Local Chef Inspired Training ;We provide six, two-hour food preparation sessions for our care-partners using local chefs, their recipes and locally grown food.

Meaningful & Engaging Activities - We provide a monthly list with local activities to our care-partners based on our client’s interest and capabilities. Focusing on what our client loved to do in the past.

Home Solutions When Needed; We provide management services to help keep our clients in their homes by working with current contractors or locating new ones to properly maintain a safe-living environment.

About owner: Dora Pruitt, owner of Willowmere Care Partners, has earned her certification as an Independent Trainer in the Bright Path; in Caregiving (BPC) by Ranella Vosk, a nationally recognized instructor on natural aging and aging with Dementia. Dora is one of five certified independent trainers in the state of Maryland. All staff will have eight hours of hands on Dementia Bright Path in Caregiving training.

On the insert 11x 4.25 want the top to be sticking out of the tri -fold "Dementia Experts . I would like to have shades of each STONE as it progresses
The Shining STONES(R): The STONES model recognizes the dynamic nature of the human brain and its abilities. Unlike other cognitive models, it acknowledges that everyone’s abilities can change in a moment. Modifying environments, situations, interactions, and expectations will create either supportive positive opportunities or result in distress and a sense of failure. Just as gemstones need different settings and care to show their best characteristics, so do people. Rather than focusing on a person’s loss when there is brain change, seeing individuals as precious, unique, and capable encourages a care partnership and is the core of this model. Providing supportive settings for everyone, including care providers, allows them to use what they have to be their best. The STONES® advocate that everyone living with brain change when given the opportunity will shine. Ranella Vosk and Bright Path in Caregiving

Sapphire ~ True Blue ~ Optimal Cognition, Healthy Brain•
True to self: personal preferences remain basically the same
• Can be flexible in thinking and appreciate multiple perspectives
• Stress/pain/fatigue may trigger Diamond state: back to Sapphire with relief
• Able to suppress and filter personal reactions: chooses effective responses
• Selects from options and can make informed decisions
• Processes well and able to successfully transition
• Aging doesn’t change ability: processing slows, more effort/time/practice needed
My brain is healthy - true blue. If I am aging normally or distressed, it may be hard for me to find words. I can describe what I am thinking so you understand. I may talk to myself because I am giving myself cues and prompts. I can learn new things and change habits, but it takes time and effort. Honoring my choices and preferences, when possible, is important. I need more time to make decisions. Give me the details and let me think about it before you need an answer. I am able to remember plans and information but supports are helpful. I may like specific prompts such as notes, calendars, and reminder calls. Health changes in vision, hearing, balance, coordination, depression, anxiety, pain, or medication may impact my behavior, but my cognitive abilities remain the same.

Diamond ~ Clear and Sharp ~ Routines and Rituals Rule
• Displays many facets: behavior and perspective can shift dramatically
• Prefers the familiar and may resist change: challenged by transitions
• More rigid and self-focused; sees wants as needs, when stressed
• Personal likes/dislikes in relationships/space/belongings etc, become more intense
• Reacts to changes in environment; benefits from familiar; functional/forgiving
• Needs repetition and time to absorb new/different information or routines
• Trusted authority figures can help: reacts better when respect is mutual
My overall cognition is clear and sharp. When happy and supported, I am capable and shine in my abilities. When distressed, I can be cutting and rigid and may see help as a threat. I have trouble seeing other points of view and may become less aware of boundaries or more possessive about my relationships, personal space, and belongings. I have many facets so people see me differently depending on the situation. This can cause conflict among my family, friends, or care team as it’s hard to tell if I am choosing my behavior or truly have limits in my ability. I can socially engage and have good cover skills. People will vary in their awareness of what is happening to me. I want to keep habits and environments as they have always been, even if they are problematic for me or others. I am often focused on the past, personal values, or finances. I will need help to make changes in my life; it’s hard for me. I can be in a Diamond state for reasons other than dementia.

Emerald ~ Green and On the Go With a Purpose ~ Naturally Flawed
• Sees self as able and independent, with limited awareness of changes in ability
• Lives in moments of clarity mixed with periods of loss in logic/reason/perspective
• Understanding and use of language change: vague words and many repeats
• Cues and support help when getting to/from places and doing daily routines
• Awareness of time, place, and situation will not always match current reality
• Strong emotional reactions are triggered by fears, desires, or unmet needs
Needs to know what comes next: seeks guidance and assistance to fill the day
I am flawed; it is part of being a natural emerald. I tend to be focused on what I want or need in this moment and may not be aware of my own safety or changing abilities. I can chat socially, but I typically miss one out of every four words and cannot accurately follow the meaning of longer conversations. I won’t remember the details of our time together, but I will remember how your body language and tone of voice made me feel. I may hide or misplace things and believe someone has taken them. My brain will make up information to fill in the blanks, which makes you think I am lying. If you try to correct me or argue, I may become resentful or suspicious of you. I am not always rational, but I don’t want to be made to feel incompetent. My brain plays tricks on me, taking me to different times and places in my life. When I am struggling, I may tell you, “I want to go home.” To provide the help and assistance I need, you must go with my flow, use a positive, partnered approach, and modify my environment.

Amber ~ Caught in a Moment of Time ~ Caution Required
• Focused on sensation: seeks to satisfy desires and tries to avoid what is disliked
•Environment can drive actions and reactions without awareness of safety
• Visual abilities are limited: focus is on pieces or parts, not the whole picture
• What happens to or around an Amber, may cause strong and surprising reactions
• Enters others’ space and crosses boundaries attempting to meet own needs
• Has periods of intense activity: may be very curious or repetitive with objects or actions
• Care is refused or seen as threatening, due to differences in perspective and ability.
Like a particle trapped in an amber, I am caught in a moment of time. It may surprise you to see how I take in the world around me. I may not know you or see you as a whole person. I react to you based on how you look, sound, move, smell, and respond to me. I like to do simple tasks over and over and may need to repeatedly move and touch, smell, taste, take or tear items apart. While it may exhaust or frustrate you, it soothes me. I don’t recognize danger; you will have to safeguard my environment. I’m intolerant to discomfort because my mouth, hands, feet, and genitalia are highly sensitive due to changes in my nervous system. Therefore, activities like eating, taking medication, mouth care, bathing, dressing, and toileting may distress me. Please notice my reaction and stop if I am resisting. I can’t help myself and one or both of us may get hurt emotionally and/or physically. If this happens, wait a few minutes, connect with me, and try a different approach; possibly substituting one area of focus for another.

Ruby ~ Deep and Strong in Color ~ Others Stop Seeing What is Possible
• Makes use of rhythm: can usually sing, hum, pray, sway, rock, clap, and dance
• When moving can’t stop; when stopped can’t get moving: needs guidance and help
• Big, strong movements are possible, while skilled abilities are being lost
• Danger exists due to limited abilities combined with automatic actions or reactions
• Tends to miss subtle hints, but gets magnified facial expressions and voice rhythms
• Can mimic actions or motions, but will struggle to understand instructions/gestures
• Able to pick up and hold objects, and yet not know what to do with them
As the deep red of a ruby masks detail, my obvious losses make my remaining abilities harder to notice. Although my fine motor skills have become very limited, remember that I am able to move and do simple things with my hands. You will need to anticipate, identify, and respond to all of my needs, even though I may not be aware of them. Plan to create a supportive environment, help with the details of care, and structure my day. Just as a crossing guard directs traffic, you will need to guide my movements and transitions. I can rarely stop or start on my own and switching gears is a challenge. Move with me first, then use your body to show me what you want me to do next, going one step at a time. Palm-beneath-Palm™ assistance helps me to feel safe and secure and to know what to do. Danger is part of my life, due to losses in visual skills, chewing abilities, balance, and coordination. You can reduce the risks to me, but not eliminate them. I can still have moments of joy when you are able to provide what gives me pleasure.

Pearl ~ Hidden Within a Shell ~ Beautiful Moments to Behold
• Will frequently recognize familiar touches, voices, faces, aromas, and tastes• Personhood survives, although all other capabilities are minimal
• Understanding input takes time: go slow and simplify for success
• In care, first get connected by offering comfort then use careful and caring touch
• Changes in the body are profound: weight loss, immobility, systems are failing
• As protective reflexes are lost, breathing, swallowing, and moving will be difficult
Care partners benefit from learning the art of letting go rather than simply giving up
While hidden like a pearl in an oyster shell, I will still have moments when I become alert and responsive. I am near the end of my life. Moments of connection create a sense of wholeness and value between us. Use our time together not just to provide care, but to comfort and connect with me. To help me complete life well, it’s important to honor my personhood when making medical or care decisions; please don’t talk about me as though I am not still here. I respond best to familiar voices and gentle rhythmic movements. I am ruled by reflexes and will startle easily. My brain is losing its ability to control and heal my body. Be prepared to see me having difficulty breathing or swallowing. My body may no longer desire food and drink as I prepare to leave this life. I may not be able to stop living without permission from you. Your greatest gift at this time in my life is to let me know that it is okay to go.

Target Market(s)

Children of seniors, seniors , rehabilitation centers

Requirements
Must have
• Nice photos of Seniors that are happy doing thing they like to do with help (Caregivers)
• Upbeat . Positive
Nice to have
• Processional looking - but very personal, we are taking care of their love ones
Should not have
• Not to feel like a cold hospital or end of life

```html
<!DOCTYPE html>
<html lang="en">
<head>
<meta charset="utf-8">
<title>Willowmere Care Partners – Brain Change Model</title>
<link rel="stylesheet" href="https://fonts.googleapis.com/css2?family=Roboto+Condensed:ital,wght@0,400;0,700;1,400&family=Roboto:wght@400;500&family=Cormorant+Garamond:ital,wght@1,700&display=swap">
<style>
  :root{
    --navy:#2b2a6b;
    --wave-blue:#1f72b4;
    --name-blue:#1d5c8e;
    --ink:#2a2a2a;
    --sapphire-top:#98b5de; --sapphire-bottom:#eef3fa;
    --emerald-top:#b9da86; --emerald-bottom:#f4f9ec;
    --ruby-top:#efa0a7;    --ruby-bottom:#fae6e8;
    --diamond-top:#c8dbe9; --diamond-bottom:#f3f7fa;
    --amber-top:#f5b567;   --amber-bottom:#fdeedd;
    --pearl-top:#efc3d7;   --pearl-bottom:#fbf0f5;
  }
  *{box-sizing:border-box;margin:0;padding:0}
  html,body{width:1200px;height:902px;overflow:hidden;background:#fff}
  .sheet{position:relative;width:1200px;height:902px;overflow:hidden;font-family:"Roboto Condensed",Arial,sans-serif;color:var(--ink)}

  .masthead{position:absolute;left:0;top:0;width:1200px;height:240px;background:var(--navy)}
  .photo{position:absolute;right:0;top:0;width:407px;height:235px;
    background:linear-gradient(135deg,#cfc9c2 0%,#e9e4de 45%,#b9a89a 100%)}
  .wave{position:absolute;left:0;top:0;z-index:3}

  .program-mark{position:absolute;left:30px;top:108px;display:flex;align-items:center;gap:10px;z-index:4}
  .program-mark .dot{width:34px;height:34px;border-radius:50%;background:#fff}
  .program-mark .name{font-family:"Roboto Condensed",Arial,sans-serif;font-weight:700;font-size:24px;color:#fff;letter-spacing:.5px}

  .intro{position:absolute;left:236px;top:70px;width:540px;z-index:4;color:#fff}
  .intro h1{font-family:"Cormorant Garamond",Georgia,serif;font-style:italic;font-weight:700;font-size:22px;margin-bottom:6px}
  .intro p{font-size:12.6px;line-height:1.3}

  .stones{position:absolute;left:0;top:215px;width:1200px;height:687px;display:grid;grid-template-columns:400px 400px 400px;grid-template-rows:340px 347px}
  .stone{overflow:hidden;padding:48px 22px 0 30px}
  .stone.lower{padding-top:24px}
  .sapphire{background:linear-gradient(var(--sapphire-top),var(--sapphire-bottom))}
  .emerald{background:linear-gradient(var(--emerald-top),var(--emerald-bottom))}
  .ruby{background:linear-gradient(var(--ruby-top),var(--ruby-bottom))}
  .diamond{background:linear-gradient(var(--diamond-top),var(--diamond-bottom))}
  .amber{background:linear-gradient(var(--amber-top),var(--amber-bottom))}
  .pearl{background:linear-gradient(var(--pearl-top),var(--pearl-bottom))}

  .stone-head{display:flex;align-items:flex-start;gap:10px;margin-bottom:12px}
  .gem{flex:none;width:40px;height:40px;border-radius:50%}
  .gem.sapphire-gem{background:radial-gradient(circle at 40% 35%,#6d7fd6,#2a2f8c)}
  .gem.emerald-gem{background:radial-gradient(circle at 40% 35%,#5ec15a,#17712b)}
  .gem.ruby-gem{background:radial-gradient(circle at 40% 35%,#f04a4f,#9c0f17)}
  .gem.diamond-gem{background:radial-gradient(circle at 40% 35%,#ffffff,#a9b3bb)}
  .gem.amber-gem{background:radial-gradient(circle at 40% 35%,#ffc54a,#d9791a)}
  .gem.pearl-gem{background:radial-gradient(circle at 40% 35%,#fbe9dd,#c79a84)}
  .stone-name{font-family:"Roboto",Arial,sans-serif;font-weight:500;font-size:18px;color:var(--name-blue);line-height:1.1}
  .stone-tag{font-style:italic;font-size:11px;color:#333;line-height:1.2;margin-top:2px}

  .traits{list-style:disc;padding-left:22px;margin-bottom:8px}
  .traits li{font-size:8.3px;line-height:12.4px}
  .voice{font-size:8.4px;line-height:11.2px}
</style>
</head>
<body>
<div class="sheet">
  <div class="masthead"></div>
  <div class="photo" role="img" aria-label="Photo of a smiling senior woman sitting with a caregiver"></div>

  <svg class="wave" width="1200" height="270" viewBox="0 0 1200 270" aria-hidden="true">
    <path d="M0 0H1200V212C1030 200 880 214 700 238C520 262 300 250 0 196Z" fill="var(--navy)" opacity="0"/>
    <path d="M0 206C300 262 520 272 700 248C880 224 1030 210 1200 222" fill="none" stroke="#ffffff" stroke-width="12"/>
    <path d="M0 192C300 248 520 258 700 234C880 210 1030 196 1200 208" fill="none" stroke="var(--wave-blue)" stroke-width="14"/>
  </svg>

  <div class="program-mark"><span class="dot"></span><span class="name">STONES</span></div>

  <div class="intro">
    <h1>Brain Change Model</h1>
    <p>The STONES® model recognizes the dynamic nature of the human brain and its abilities. Unlike other cognitive models, it acknowledges that everyone’s abilities can change in a moment. Modifying environments, situations, interactions, and expectations will create either supportive positive opportunities or result in distress and a sense of failure. Just as gemstones need different settings and care to show their best characteristics, so do people. Rather than focusing on a person’s loss when there is brain change, seeing individuals as precious, unique, and capable encourages a care partnership and is the core of this model. Providing supportive settings for everyone,</p>
  </div>

  <main class="stones">
    <section class="stone sapphire">
      <div class="stone-head"><div class="gem sapphire-gem" role="img" aria-label="Sapphire gemstone illustration"></div>
        <div><h2 class="stone-name">Sapphire ~</h2><p class="stone-tag">True Blue ~ Optimal Cognition, Healthy Brain</p></div></div>
      <ul class="traits">
        <li>True to self: personal preferences remain basically the same</li>
        <li>Can be flexible in thinking and appreciate multiple perspectives</li>
        <li>Stress/pain/fatigue may trigger Diamond state: back to Sapphire with relief</li>
        <li>Able to suppress and filter personal reactions: chooses effective responses</li>
        <li>Selects from options and can make informed decisions</li>
        <li>Processes well and able to successfully transition</li>
        <li>Aging doesn’t change ability: processing slows, more effort/time/practice needed</li>
      </ul>
      <p class="voice">My brain is healthy - true blue. If I am aging normally or distressed, it may be hard for me to find words. I can describe what I am thinking so you understand. I may talk to myself because I am giving myself cues and prompts. I can learn new things and change habits, but it takes time and effort. Honoring my choices and preferences, when possible, is important. I need more time to make decisions. Give me the details and let me think about it before you need an answer. I am able to remember plans and information but supports are helpful. I may like specific prompts such as notes, calendars, and reminder calls. Health changes in vision, hearing, balance, coordination, depression, anxiety, pain, or medication may impact my behavior, but my cognitive abilities remain the same.</p>
    </section>

    <section class="stone emerald">
      <div class="stone-head"><div class="gem emerald-gem" role="img" aria-label="Emerald gemstone illustration"></div>
        <div><h2 class="stone-name">Emerald~</h2><p class="stone-tag">Green and On the Go With a Purpose ~ Naturally Flawed</p></div></div>
      <ul class="traits">
        <li>Sees self as able and independent, with limited awareness of changes in ability</li>
        <li>Lives in moments of clarity mixed with periods of loss in logic/reason/perspective</li>
        <li>Understanding and use of language change: vague words and many repeats</li>
        <li>Cues and support help when getting to/from places and doing daily routines</li>
        <li>Awareness of time, place, and situation will not always match current reality</li>
        <li>Strong emotional reactions are triggered by fears, desires, or unmet needs</li>
      </ul>
      <p class="voice">Needs to know what comes next: seeks guidance and assistance to fill the day<br>I am flawed; it is part of being a natural emerald. I tend to be focused on what I want or need in this moment and may not be aware of my own safety or changing abilities. I can chat socially, but I typically miss one out of every four words and cannot accurately follow the meaning of longer conversations. I won’t remember the details of our time together, but I will remember how your body language and tone of voice made me feel. I may hide or misplace things and believe someone has taken them. My brain will make up information to fill in the blanks, which makes you think I am lying. If you try to correct me or argue, I may become resentful or suspicious of you. I am not always rational, but I don’t want to be made to feel incompetent. My brain plays tricks on me, taking me to different times and places in my life. When I am struggling, I may tell you, “I want to go home.” To provide the help and assistance I need, you must go with my flow, use a positive, partnered approach, and modify my environment.</p>
    </section>

    <section class="stone ruby">
      <div class="stone-head"><div class="gem ruby-gem" role="img" aria-label="Ruby gemstone illustration"></div>
        <div><h2 class="stone-name">Ruby~</h2><p class="stone-tag">Deep and Strong in Color ~ Others Stop Seeing<br>What is Possible</p></div></div>
      <ul class="traits">
        <li>Makes use of rhythm: can usually sing, hum, pray, sway, rock, clap, and dance</li>
        <li>When moving can’t stop; when stopped can’t get moving: needs guidance and help</li>
        <li>Big, strong movements are possible, while skilled abilities are being lost</li>
        <li>Danger exists due to limited abilities combined with automatic actions or reactions</li>
        <li>Tends to miss subtle hints, but gets magnified facial expressions and voice rhythms</li>
        <li>Can mimic actions or motions, but will struggle to understand instructions/gestures</li>
        <li>Able to pick up and hold objects, and yet not know what to do with them</li>
      </ul>
      <p class="voice">As the deep red of a ruby masks detail, my obvious losses make my remaining abilities harder to notice. Although my fine motor skills have become very limited, remember that I am able to move and do simple things with my hands. You will need to anticipate, identify, and respond to all of my needs, even though I may not be aware of them. Plan to create a supportive environment, help with the details of care, and structure my day. Just as a crossing guard directs traffic, you will need to guide my movements and transitions. I can rarely stop or start on my own and switching gears is a challenge. Move with me first, then use your body to show me what you want me to do next, going one step at a time. Palm-beneath-Palm™ assistance helps me to feel safe and secure and to know what to do. Danger is part of my life, due to losses in visual skills, chewing abilities, balance, and coordination. You can reduce the risks to me, but not eliminate them. I can still have moments of joy when you are able to provide what gives me pleasure.</p>
    </section>

    <section class="stone diamond lower">
      <div class="stone-head"><div class="gem diamond-gem" role="img" aria-label="Diamond gemstone illustration"></div>
        <div><h2 class="stone-name">Diamond~</h2><p class="stone-tag">Clear and Sharp ~ Routines and Rituals Rule</p></div></div>
      <ul class="traits">
        <li>Displays many facets: behavior and perspective can shift dramatically</li>
        <li>Prefers the familiar and may resist change: challenged by transitions</li>
        <li>More rigid and self-focused; sees wants as needs, when stressed</li>
        <li>Personal likes/dislikes in relationships/space/belongings etc, become more intense</li>
        <li>Reacts to changes in environment; benefits from familiar; functional/forgiving</li>
        <li>Needs repetition and time to absorb new/different information or routines</li>
        <li>Trusted authority figures can help: reacts better when respect is mutual</li>
      </ul>
      <p class="voice">My overall cognition is clear and sharp. When happy and supported, I am capable and shine in my abilities. When distressed, I can be cutting and rigid and may see help as a threat. I have trouble seeing other points of view and may become less aware of boundaries or more possessive about my relationships, personal space, and belongings. I have many facets so people see me differently depending on the situation. This can cause conflict among my family, friends, or care team as it’s hard to tell if I am choosing my behavior or truly have limits in my ability. I can socially engage and have good cover skills. People will vary in their awareness of what is happening to me. I want to keep habits and environments as they have always been, even if they are problematic for me or others. I am often focused on the past, personal values, or finances. I will need help to make changes in my life; it’s hard for me. I can be in a Diamond state for reasons other than dementia.</p>
    </section>

    <section class="stone amber lower">
      <div class="stone-head"><div class="gem amber-gem" role="img" aria-label="Amber gemstone illustration"></div>
        <div><h2 class="stone-name">Amber ~</h2><p class="stone-tag">Caught in a Moment of Time ~ Caution Required</p></div></div>
      <ul class="traits">
        <li>Focused on sensation: seeks to satisfy desires and tries to avoid what is disliked</li>
        <li>Environment can drive actions and reactions without awareness of safety</li>
        <li>Visual abilities are limited: focus is on pieces or parts, not the whole picture</li>
        <li>What happens to or around an Amber, may cause strong and surprising reactions</li>
        <li>Enters others’ space and crosses boundaries attempting to meet own needs</li>
        <li>Has periods of intense activity: may be very curious or repetitive with objects or actions</li>
        <li>Care is refused or seen as threatening, due to differences in perspective and ability</li>
      </ul>
      <p class="voice">Like a particle trapped in an amber, I am caught in a moment of time. It may surprise you to see how I take in the world around me. I may not know you or see you as a whole person. I react to you based on how you look, sound, move, smell, and respond to me. I like to do simple tasks over and over and may need to repeatedly move and touch, smell, taste, take or tear items apart. While it may exhaust or frustrate you, it soothes me. I don’t recognize danger; you will have to safeguard my environment. I’m intolerant to discomfort because my mouth, hands, feet, and genitalia are highly sensitive due to changes in my nervous system. Therefore, activities like eating, taking medication, mouth care, bathing, dressing, and toileting may distress me. Please notice my reaction and stop if I am resisting. I can’t help myself and one or both of us may get hurt emotionally and/or physically. If this happens, wait a few minutes, connect with me, and try a different approach; possibly substituting one area of focus for another.</p>
    </section>

    <section class="stone pearl lower">
      <div class="stone-head"><div class="gem pearl-gem" role="img" aria-label="Pearl illustration"></div>
        <div><h2 class="stone-name">Pearl ~</h2><p class="stone-tag">Hidden Within a Shell ~ Beautiful Moments to Behold</p></div></div>
      <ul class="traits">
        <li>Will frequently recognize familiar touches, voices, faces, aromas, and tastes</li>
        <li>Personhood survives, although all other capabilities are minimal</li>
        <li>Understanding input takes time: go slow and simplify for success</li>
        <li>In care, first get connected by offering comfort then use careful and caring touch</li>
        <li>Changes in the body are profound: weight loss, immobility, systems are failing</li>
        <li>As protective reflexes are lost, breathing, swallowing, and moving will be difficult</li>
        <li>Care partners benefit from learning the art of letting go rather than simply giving up</li>
      </ul>
      <p class="voice">While hidden like a pearl in an oyster shell, I will still have moments when I become alert and responsive. I am near the end of my life. Moments of connection create a sense of wholeness and value between us. Use our time together not just to provide care, but to comfort and connect with me. To help me complete life well, it’s important to honor my personhood when making medical or care decisions; please don’t talk about me as though I am not still here. I respond best to familiar voices and gentle rhythmic movements. I am ruled by reflexes and will startle easily. My brain is losing its ability to control and heal my body. Be prepared to see me having difficulty breathing or swallowing. My body may no longer desire food and drink as I prepare to leave this life. I may not be able to stop living without permission from you. Your greatest gift at this time in my life is to let me know that it is okay to go.</p>
    </section>
  </main>
</div>
</body>
</html>
```